Website re-design

We are a successful furnished apartment provider in Boston. We currently are working on re-designing our website www.ribtenlofts.com to make it more modern, designer look and user friendly. We hired a designer, but are not happy with the designs proposed and want to improve on them. The winning design will be paid regardless of whether we stay with our current designer or not. We want ideas and functional page links to see how it will work. Platform we have chosen is wordpress. Feel free to propose others easy for us to update and modify. We do not like Joomla on which website is currently running. We do not like flash nor long load times.
Please use photos on our website for design presentations. www.ribtenlofts.com

Target Market(s)

doctors, nurses, business men but mostly business women, some post-medical students

Industry/Entity Type

Apartment

Requirements
Must have
• Quick action button for reservation form and a notification and email forwarding system to us of reservation information by potential clients. Blog required with feedback by guests allowed, we can censor which are published. Slide shows of apartments.
Should not have
• No movies.

```html
<!DOCTYPE html>
<html lang="en">
<head>
<meta charset="utf-8">
<title>Ribten Lofts – Footer</title>
<link rel="stylesheet" href="https://fonts.googleapis.com/css2?family=Ubuntu&family=Didact+Gothic&family=Arimo:wght@400;700&display=swap">
<style>
  :root {
    --page-bg: #f3f3f3;
    --intro-text: #555555;
    --footer-bg: #282828;
    --footer-text: #ffffff;
    --footer-muted: #cfcfcf;
    --rule: #0f0f0f;
    --link-muted: #9a9a9a;
    --bar-dark: #000000;
    --bottom-strip: #e4e4e4;
  }
  html, body { margin: 0; padding: 0; }
  body {
    width: 1200px; height: 626px; overflow: hidden; position: relative;
    background: var(--page-bg);
  }
  .intro {
    position: absolute; left: 145px; top: -21px; width: 860px; margin: 0;
    font-family: "Ubuntu", sans-serif; font-size: 23.5px; line-height: 35.5px;
    color: var(--intro-text);
  }
  .top-bar {
    position: absolute; left: 0; top: 282px; width: 1200px; height: 9px;
    background: linear-gradient(90deg, var(--bar-dark) 0%, #1a1a1a 40%, #6a6a6a 55%, #1a1a1a 70%, var(--bar-dark) 100%);
  }
  .top-bar::after {
    content: ""; position: absolute; left: 0; top: 9px; width: 100%; height: 1px; background: #ffffff;
  }
  .site-footer {
    position: absolute; left: 0; top: 293px; width: 1200px; height: 319px;
    background: var(--footer-bg); color: var(--footer-text);
    font-family: "Arimo", sans-serif; font-size: 12px;
  }
  .bottom-strip {
    position: absolute; left: 0; top: 612px; width: 1200px; height: 14px; background: var(--bottom-strip);
  }
  .footer-col { position: absolute; top: 15px; width: 205px; }
  .col-disclaimer { left: 140px; }
  .col-about { left: 379px; }
  .col-contact { left: 616px; }
  .col-signup { left: 853px; }
  .footer-col h2 {
    margin: 0; padding-bottom: 3px; border-bottom: 1px solid var(--rule);
    font-family: "Didact Gothic", sans-serif; font-weight: 400; font-size: 23px;
    letter-spacing: -0.5px; line-height: 30px; color: var(--footer-text);
    box-shadow: 0 1px 0 #3a3a3a;
  }
  .footer-col p { margin: 8px 0 0; line-height: 24px; }
  .col-about p { margin-top: 5px; }
  .site-url {
    margin-top: 4px; font-family: "Arimo", sans-serif; font-weight: 700;
    font-size: 13px; letter-spacing: 0.3px;
  }
  .contact-list { list-style: none; margin: 0; padding: 0; }
  .contact-list li { padding-left: 16px; position: relative; line-height: 24px; }
  .contact-list li::before {
    content: ""; position: absolute; left: 0; top: 8px; width: 0; height: 0;
    border-left: 5px solid #8a8a8a; border-top: 4px solid transparent; border-bottom: 4px solid transparent;
    box-shadow: none;
  }
  .contact-list li::after {
    content: ""; position: absolute; left: 5px; top: 8px; width: 0; height: 0;
    border-left: 5px solid #8a8a8a; border-top: 4px solid transparent; border-bottom: 4px solid transparent;
  }
  .social-row { display: flex; gap: 7px; margin: 18px 0 0 14px; }
  .social-row span { width: 24px; height: 18px; border-radius: 3px; display: block; }
  .signup-buttons { margin: 25px 0 0 44px; display: flex; flex-direction: column; gap: 1px; }
  .signup-button {
    width: 142px; height: 34px; border-radius: 3px; box-sizing: border-box;
    border: 1px solid #6a6a6a;
    font-family: "Didact Gothic", sans-serif; font-size: 24px; letter-spacing: 1px;
    text-align: center; line-height: 33px; color: #666;
  }
  .signup-button.light { background: linear-gradient(#f4f4f4, #bdbdbd); }
  .signup-button.dark { background: linear-gradient(#8f8f8f, #4e4e4e); color: #2e2e2e; }
  .footer-rule {
    position: absolute; left: 140px; top: 240px; width: 922px; height: 1px;
    background: var(--rule); box-shadow: 0 1px 0 #353535;
  }
  .copyright {
    position: absolute; left: 140px; top: 279px; font-size: 11px; color: var(--footer-muted);
  }
  .back-to-top {
    position: absolute; left: 1000px; top: 276px; font-size: 11.5px;
    color: var(--link-muted); text-decoration: underline;
  }
</style>
</head>
<body>
  <p class="intro">In the South End neighborhood, you will find wonderful restaurants, theaters, cafes and artist lofts. Our short term and extended stay apartments are very, very clean. We also offer the latest designer layouts: hardwood floors, Wireless Dsl, Cable TV, flat screen in most apartments, washer and dryer, cookware, cotton linens. Please click links on left for photo galleries, pricing, availability and reservation form and write us for more information.<br>Thank you.</p>

  <div class="top-bar"></div>

  <footer class="site-footer">
    <section class="footer-col col-disclaimer">
      <h2>Disclaimer</h2>
      <p>Important: Lorem ipsum dolor sit am adipisicing elit, sed do eiusmod tem incididunt ut labore et dolore magna Ut enim ad minim veniam, quis nost exercitation.</p>
    </section>

    <section class="footer-col col-about">
      <h2>About</h2>
      <p>Lorem ipsum dolor sit amet, consect adipisicing elit, sed do eiusmod tem incididunt ut labore et dolore magna Ut enim ad minim veniam, quis nost exercitation.</p>
      <div class="site-url">www.ribtenlofts.com</div>
    </section>

    <section class="footer-col col-contact">
      <h2>Contact</h2>
      <p style="margin-top:6px;line-height:22px;white-space:nowrap">Technical support: example@email.com</p>
      <ul class="contact-list">
        <li>General Information</li>
        <li>Frequently Asked Questions</li>
        <li>Member Support Forum</li>
      </ul>
      <div class="social-row" role="img" aria-label="Social sharing buttons">
        <span style="background:#d9d9d9"></span>
        <span style="background:#5aa9d6"></span>
        <span style="background:#e0801f"></span>
        <span style="background:#8cb05a"></span>
        <span style="background:#6e7f94"></span>
        <span style="background:#3b5a98"></span>
      </div>
    </section>

    <section class="footer-col col-signup">
      <h2>Sign Up Today</h2>
      <p>Get the latest news and events by subscribing up for our newsletter</p>
      <div class="signup-buttons">
        <div class="signup-button light">SIGN UP</div>
        <div class="signup-button dark">SIGN UP</div>
      </div>
    </section>

    <div class="footer-rule"></div>
    <div class="copyright">©Ribten Lofts 2010 - All Rights Reserved</div>
    <a class="back-to-top">Back to top</a>
  </footer>

  <div class="bottom-strip"></div>
</body>
</html>
```